LED Bulb Packaging

We require a retail box design so some led lighting. The concept must be uniform accross a nuimber of sizes with technical information and Actual bulb image replaceable.

```html
<!DOCTYPE html>
<html lang="en">
<head>
<meta charset="utf-8">
<title>Corn LED 27W – Retail Box Panels</title>
<link rel="stylesheet" href="https://fonts.googleapis.com/css2?family=Montserrat:wght@700;800;900&family=Roboto+Condensed:wght@400;700&family=Oswald:wght@500&display=swap">
<style>
  :root{
    --red:#d71920;
    --red-dark:#b5121a;
    --grey:#6b6b6b;
    --grey-dark:#4f4f4f;
    --paper:#ececec;
    --white:#ffffff;
    --ink:#111111;
    --bg:#ffffff;
  }
  *{margin:0;padding:0;box-sizing:border-box}
  html,body{width:1200px;height:857px;overflow:hidden;background:var(--bg)}
  .canvas{position:relative;width:1200px;height:857px}

  .side-panel{position:absolute;left:120px;top:228px;width:180px;height:400px;background:var(--red);overflow:hidden}
  .side-panel svg{position:absolute;inset:0}
  .side-wattage{position:absolute;left:0;right:0;top:150px;text-align:center;
    font-family:"Oswald",sans-serif;font-weight:500;font-size:74px;letter-spacing:-1px;color:var(--ink);
    transform:scaleX(.8)}
  .side-specs{position:absolute;left:10px;top:318px;font-family:"Roboto Condensed",sans-serif;font-size:12px;color:var(--ink);word-spacing:8px}

  .front-panel{position:absolute;left:300px;top:228px;width:780px;height:400px;background:var(--paper);overflow:hidden}
  .front-panel > svg{position:absolute;inset:0}

  .brand-title{position:absolute;left:46px;top:34px;font-family:"Montserrat",sans-serif;font-weight:900;
    font-size:96px;line-height:1;letter-spacing:2px;color:var(--red)}
  .product-name{position:absolute;left:48px;top:128px;font-family:"Montserrat",sans-serif;font-weight:800;
    font-size:30px;letter-spacing:2px;color:var(--ink)}

  .spec{position:absolute;font-family:"Roboto Condensed",sans-serif;color:var(--white)}
  .spec-value{font-size:28px;font-weight:400;color:var(--red);line-height:1}
  .spec-label{font-size:12px;letter-spacing:.3px;margin-top:2px}
  .spec-upto{display:inline-block;font-size:10px;line-height:1;vertical-align:middle;margin-right:4px;color:var(--white)}

  .bulb-image{position:absolute;left:500px;top:40px;width:260px;height:240px;border-radius:40px 70px 70px 40px;
    background:radial-gradient(ellipse at 40% 45%,#f4f4f4 0%,#c9c9c9 45%,#7a7a7a 80%,#3c3c3c 100%);
    transform:rotate(-12deg)}

  .cert-row{position:absolute;left:50px;top:318px;display:flex;gap:22px;align-items:center}
  .cert-badge{width:34px;height:34px;border-radius:50%;border:2px solid var(--red-dark);background:rgba(255,255,255,.12)}
  .cert-badge.square{border-radius:3px}
</style>
</head>
<body>
<div class="canvas">

  <section class="side-panel">
    <svg width="180" height="400" viewBox="0 0 180 400" aria-hidden="true">
      <polygon points="180,290 180,400 60,400" fill="var(--white)"/>
      <polygon points="0,0 40,0 0,30" fill="var(--red-dark)"/>
    </svg>
    <div class="side-wattage">27W</div>
    <div class="side-specs">50000hrs IP64 120lm/w</div>
  </section>

  <section class="front-panel">
    <svg width="780" height="400" viewBox="0 0 780 400" aria-hidden="true">
      <!-- top-right red chevron -->
      <polygon points="600,0 780,0 780,130 690,170" fill="var(--red)"/>
      <polygon points="740,0 780,0 780,40" fill="var(--grey-dark)"/>
      <!-- grey spec band -->
      <polygon points="0,168 780,150 780,290 0,300" fill="var(--grey)"/>
      <polygon points="560,160 780,150 780,290 700,292" fill="var(--grey-dark)"/>
      <!-- red certification band -->
      <polygon points="0,300 780,290 780,345 0,360" fill="var(--red)"/>
      <!-- bottom white strip with red corner -->
      <polygon points="0,360 780,345 780,400 0,400" fill="var(--white)"/>
      <polygon points="0,360 60,358 0,400" fill="var(--red)"/>
    </svg>

    <div class="brand-title">LED</div>
    <div class="product-name">CORN LED</div>

    <div class="spec" style="left:48px;top:186px">
      <div class="spec-value">120lm/w</div>
      <div class="spec-label">Luminous efficiency</div>
    </div>
    <div class="spec" style="left:204px;top:186px">
      <div class="spec-value"><span class="spec-upto">UP<br>TO</span>85%</div>
      <div class="spec-label">Energy Saving</div>
    </div>
    <div class="spec" style="left:48px;top:240px">
      <div class="spec-value">50000hrs</div>
      <div class="spec-label">Lifespan</div>
    </div>
    <div class="spec" style="left:204px;top:240px">
      <div class="spec-value">IP64</div>
    </div>

    <div class="bulb-image" role="img" aria-label="Product photo of a silver corn LED bulb with rows of LED chips and a screw base"></div>

    <div class="cert-row">
      <div class="cert-badge"></div>
      <div class="cert-badge"></div>
      <div class="cert-badge square"></div>
      <div class="cert-badge"></div>
      <div class="cert-badge"></div>
      <div class="cert-badge square"></div>
    </div>
  </section>

</div>
</body>
</html>
```